Derek Hollins Business card

Hey there, I’m hoping to have a business card designed. I’m in Real estate and just switched to a new Brokerage called: The Property Quarter

The back could just be the company name maybe or whatever looks good!

I’ve attached some logos of our company and some cards my buddy had done up.

On the card:
Derek Hollins
derekhollins@mailbox-demo.com
587-214-6093
derekhollins-demo.ca

Target Market(s)

Home buyers and sellers

Industry/Entity Type

Real Estate

Contact Information for Business Card

just looking for a cool and modern design with my picture on it. I like the idea of Black and red being used.

Requirements
Must have
• all the details provided. I'm open to anything. Just want a professional looking card.

```html
<!DOCTYPE html>
<html lang="en">
<head>
<meta charset="utf-8">
<title>Derek Hollins – Business Card</title>
<link href="https://fonts.googleapis.com/css2?family=Fira+Sans:wght@600&family=Montserrat:wght@400;800&display=swap" rel="stylesheet">
<style>
  :root {
    --page: #e9e8ea;
    --ink: #07090b;
    --paper: #ffffff;
    --red: #d4213d;
    --photo-top: #4a4f57;
    --photo-bottom: #1c2026;
  }
  * { box-sizing: border-box; margin: 0; padding: 0; }
  html, body { width: 1200px; height: 1108px; overflow: hidden; background: var(--page); }
  body { position: relative; font-family: "Montserrat", sans-serif; }

  .card {
    position: absolute; left: 236px; width: 750px; height: 458px; overflow: hidden;
    box-shadow: 0 8px 22px rgba(0,0,0,0.18);
  }
  .card-front { top: 61px; background: var(--ink); }
  .card-back { top: 581px; height: 440px; background: var(--ink); }

  .front-band { position: absolute; left: 0; top: 0; width: 100%; height: 218px; background: var(--paper); }

  .wordmark {
    font-family: "Montserrat", sans-serif; font-weight: 800;
    letter-spacing: 0.3px; line-height: 1.1; display: flex; align-items: flex-start; gap: 14px;
  }
  .wordmark-name span { display: block; white-space: nowrap; }
  .wordmark-mark { width: 18px; height: 18px; background: var(--red); flex: none; margin-top: 0.4em; }
  .front-wordmark { position: absolute; left: 38px; top: 58px; font-size: 42px; color: var(--ink); }
  .back-wordmark {
    position: absolute; left: 0; right: 0; top: 0; bottom: 0;
    justify-content: center; align-items: center; font-size: 50px; color: var(--paper);
  }
  .back-wordmark .wordmark-mark { margin-top: 0; align-self: flex-start; margin-top: 168px; }

  .portrait {
    position: absolute; left: 412px; top: 12px; width: 290px; height: 446px;
    border-radius: 120px 120px 0 0;
    background: linear-gradient(180deg, var(--photo-top), var(--photo-bottom));
  }

  .agent { position: absolute; left: 33px; top: 244px; color: var(--paper); }
  .agent-name { font-family: "Fira Sans", sans-serif; font-weight: 600; font-size: 28px; color: var(--red); line-height: 1.1; }
  .agent-title { font-size: 16px; margin-top: 5px; }

  .contacts { position: absolute; left: 33px; top: 328px; list-style: none; color: var(--paper); font-size: 16.5px; }
  .contacts li { display: flex; align-items: center; gap: 11px; height: 33px; }
  .contacts svg { width: 16px; height: 16px; flex: none; fill: var(--red); }
</style>
</head>
<body>
  <section class="card card-front">
    <div class="front-band"></div>
    <div class="wordmark front-wordmark">
      <span class="wordmark-mark"></span>
      <div class="wordmark-name"><span>The Property</span><span>Quarter</span></div>
    </div>
    <div class="portrait" role="img" aria-label="Portrait photo of Derek Hollins in a dark suit and white shirt"></div>
    <div class="agent">
      <h1 class="agent-name">Derek Hollins</h1>
      <p class="agent-title">Owner</p>
    </div>
    <ul class="contacts">
      <li>
        <svg viewBox="0 0 16 16" aria-hidden="true"><path d="M3.6 1.2l2.2 2.9-1.3 1.8c.9 2 2.6 3.7 4.6 4.6l1.8-1.3 2.9 2.2-1.2 2.4C6.8 13.6 2.4 9.2 1.2 3.4z"/></svg>
        587-214-6093
      </li>
      <li>
        <svg viewBox="0 0 16 16" aria-hidden="true"><path d="M1 3.5h14v1.2L8 9 1 4.7zM1 6.3l7 4.3 7-4.3v6.2H1z"/></svg>
        derekhollins@mailbox-demo.com
      </li>
      <li>
        <svg viewBox="0 0 16 16" aria-hidden="true"><circle cx="8" cy="8" r="7"/><path d="M4 4.5c1.5.3 2 1.5 1.4 2.5-.6 1-1.8.8-1.8 2.4 0 1 .8 1.5 1.2 2.8M9.5 2c-.3 1.5.8 2.3 2 2 1 .7.5 2-.4 2.3-1.2.4-1.6 1.5-.6 2.7" fill="none" stroke="#07090b" stroke-width="1.1"/></svg>
        www.derekhollins-demo.ca
      </li>
    </ul>
  </section>

  <section class="card card-back">
    <div class="wordmark back-wordmark">
      <span class="wordmark-mark"></span>
      <div class="wordmark-name"><span>The Property</span><span>Quarter</span></div>
    </div>
  </section>
</body>
</html>
```